Graduation Day Sale Banner Ad for Website

We need a banner for our upscale jewelry website. Banner must have a classy high end look. The size of the banner must be 1187 × 400. I have attached pieces we would like used (some or all). The banner is for a Graduation Day sale that we are running. The banner should say "Graduation Day Gifts on Sale"

Target Market(s)

Wealthy individuals looking to buy graduation gifts for their children

Industry/Entity Type

Jewelry

Requirements
Must have
• Must match the look and feel of the website (www.velmira-studio.com)

```html
<!DOCTYPE html>
<html lang="en">
<head>
<meta charset="utf-8">
<title>Velmira – Fine Estate and Designer Jewelry</title>
<link rel="stylesheet" href="https://fonts.googleapis.com/css2?family=Open+Sans:wght@400;600&family=Josefin+Sans:wght@300;400&family=Great+Vibes&display=swap">
<style>
  :root {
    --page: #ffffff;
    --ink: #4a4a4a;
    --ink-soft: #6b6b6b;
    --icon: #a58a78;
    --nav: #9b8170;
    --nav-text: #ffffff;
    --rule: #8d8d8d;
    --corner: #f1d9a8;
    --peach-light: #fcf1ea;
    --peach: #f8dfd0;
    --peach-deep: #f4d0bb;
    --headline: #8a5843;
    --headline-soft: #9c6a55;
  }
  * { box-sizing: border-box; margin: 0; padding: 0; }
  html, body { width: 1200px; height: 604px; overflow: hidden; background: var(--page); }
  body { position: relative; font-family: "Open Sans", Arial, sans-serif; color: var(--ink); }

  .signup-corner { position: absolute; top: 0; right: 18px; width: 113px; height: 113px; }

  .utility-item { position: absolute; top: 55px; display: flex; align-items: center; gap: 10px; font-size: 14px; letter-spacing: 1px; color: var(--ink-soft); line-height: 20px; }
  .utility-item svg { width: 17px; height: 17px; }
  .utility-item.phone { left: 574px; }
  .utility-item.sell { left: 763px; }
  .utility-item.account { left: 935px; font-size: 11px; letter-spacing: 1.2px; }

  .brand { position: absolute; left: 99px; top: 130px; width: 326px; }
  .brand-name { font-family: "Josefin Sans", Arial, sans-serif; font-weight: 300; font-size: 60px; letter-spacing: 7px; color: #1c1c1c; line-height: 1; }
  .brand-tagline { margin-top: 4px; font-family: "Josefin Sans", Arial, sans-serif; font-weight: 400; font-size: 16.5px; letter-spacing: 0.3px; color: #1c1c1c; white-space: nowrap; }

  .search { position: absolute; left: 527px; top: 98px; width: 279px; height: 27px; border-bottom: 1px solid var(--rule); display: flex; align-items: center; }
  .search svg.lens { width: 15px; height: 15px; margin-left: 10px; }
  .search span { margin-left: 17px; font-size: 11px; color: var(--ink); }
  .search .submit { position: absolute; right: 0; top: 0; width: 27px; height: 27px; background: var(--nav); display: flex; align-items: center; justify-content: center; }

  .quick-link { position: absolute; top: 90px; width: 90px; text-align: center; font-size: 10.5px; letter-spacing: 1.2px; color: var(--ink-soft); }
  .quick-link svg { display: block; margin: 0 auto 7px; width: 23px; height: 21px; }
  .quick-link.newsletter { left: 844px; }
  .quick-link.wishlist { left: 937px; }
  .quick-link.cart { left: 1015px; }
  .quick-link small { font-size: 8.5px; }

  .main-nav { position: absolute; left: 447px; top: 155px; height: 41px; display: flex; gap: 1px; }
  .main-nav a { display: flex; align-items: center; justify-content: center; height: 41px; background: var(--nav); color: var(--nav-text); text-decoration: none; font-size: 15px; letter-spacing: 0.8px; }
  .nav-fine { width: 147px; }
  .nav-time { width: 132px; }
  .nav-acc { width: 145px; }
  .nav-des { width: 129px; }
  .nav-sale { width: 79px; }

  .hero { position: absolute; left: 97px; top: 243px; width: 988px; height: 333px; overflow: hidden;
    background:
      radial-gradient(ellipse 40% 55% at 72% 55%, var(--peach-light) 0%, transparent 100%),
      linear-gradient(180deg, var(--peach) 0%, var(--peach-deep) 100%); }
  .hero-products { position: absolute; left: 150px; top: 0; width: 380px; height: 333px;
    background:
      radial-gradient(ellipse 30% 22% at 37% 33%, rgba(205,205,212,0.95) 0%, rgba(205,205,212,0.5) 55%, transparent 100%),
      radial-gradient(ellipse 32% 24% at 62% 66%, rgba(214,178,96,0.95) 0%, rgba(214,178,96,0.45) 60%, transparent 100%),
      radial-gradient(ellipse 22% 26% at 30% 80%, rgba(236,226,214,0.95) 0%, rgba(225,190,120,0.5) 55%, transparent 100%); }
  .hero-copy { position: absolute; left: 551px; top: 104px; }
  .hero-script { font-family: "Great Vibes", cursive; font-size: 62px; color: var(--headline-soft); line-height: 1; white-space: nowrap; }
  .hero-gift { margin: -4px 0 0 52px; font-family: "Josefin Sans", Arial, sans-serif; font-weight: 300; font-size: 33px; letter-spacing: 0.5px; color: var(--headline); line-height: 1; }
  .hero-sale { margin: 6px 0 0 50px; font-family: "Josefin Sans", Arial, sans-serif; font-weight: 300; font-size: 76px; letter-spacing: 1px; color: var(--headline); line-height: 0.9; }
  .hero-cap { position: absolute; left: 770px; top: 116px; width: 108px; height: 70px;
    background: radial-gradient(ellipse 50% 50% at 50% 50%, rgba(212,170,100,0.85) 0%, rgba(212,170,100,0.4) 55%, transparent 100%); }
</style>
</head>
<body>

  <svg class="signup-corner" viewBox="0 0 113 113" aria-label="Sign up">
    <polygon points="0,0 113,0 113,113" fill="var(--corner)"/>
    <polygon points="90,26 97,26 97,33" fill="#1c1c1c"/>
    <text x="66" y="50" transform="rotate(45 66 50)" font-family="Open Sans, sans-serif" font-size="14" fill="#3a3a3a" text-anchor="middle">Sign up!</text>
  </svg>

  <div class="utility-item phone">
    <svg viewBox="0 0 24 24" fill="none" stroke="var(--icon)" stroke-width="1.5"><path d="M5 3h4l2 5-2.5 1.5a11 11 0 0 0 6 6L16 13l5 2v4a2 2 0 0 1-2 2A17 17 0 0 1 3 5a2 2 0 0 1 2-2z"/></svg>
    <span>800 - 555 - 0142</span>
  </div>
  <div class="utility-item sell">
    <svg viewBox="0 0 24 24" fill="none" stroke="var(--icon)" stroke-width="1.3"><path d="M3 9l4-5h10l4 5-9 11z M3 9h18 M9 4l3 5 3-5 M12 9v11"/></svg>
    <span>SELL JEWELRY</span>
  </div>
  <div class="utility-item account">
    <svg viewBox="0 0 24 24" fill="none" stroke="var(--icon)" stroke-width="1.3"><circle cx="12" cy="8" r="4.5"/><path d="M3 22c0-5 4-8 9-8s9 3 9 8z"/></svg>
    <span>SIGN IN / REGISTER</span>
  </div>

  <div class="brand">
    <div class="brand-name">VELMIRA</div>
    <div class="brand-tagline">FINE ESTATE AND DESIGNER JEWELRY</div>
  </div>

  <div class="search">
    <svg class="lens" viewBox="0 0 16 16" fill="none" stroke="var(--icon)" stroke-width="1.3"><circle cx="6.5" cy="6.5" r="5"/><path d="M10.5 10.5l4 4"/></svg>
    <span>Search</span>
    <div class="submit">
      <svg width="13" height="11" viewBox="0 0 13 11" fill="none" stroke="#fff" stroke-width="2.2"><path d="M1 5.5l3.8 3.8L12 1.5"/></svg>
    </div>
  </div>

  <div class="quick-link newsletter">
    <svg viewBox="0 0 24 22" fill="none" stroke="var(--icon)" stroke-width="1.3"><rect x="1.5" y="4" width="21" height="14"/><path d="M1.5 4l10.5 8 10.5-8"/></svg>
    NEWSLETTER
  </div>
  <div class="quick-link wishlist">
    <svg viewBox="0 0 24 22" fill="none" stroke="var(--icon)" stroke-width="1.3"><path d="M12 20S2 13.5 2 7.5A5 5 0 0 1 12 5a5 5 0 0 1 10 2.5C22 13.5 12 20 12 20z"/></svg>
    WISHLIST
  </div>
  <div class="quick-link cart">
    <svg viewBox="0 0 24 22" fill="none" stroke="var(--icon)" stroke-width="1.3"><path d="M2 2h3l3 12h11l2-8H7"/><circle cx="9" cy="18.5" r="1.6"/><circle cx="17" cy="18.5" r="1.6"/></svg>
    CART <small>(0)</small>
  </div>

  <nav class="main-nav">
    <a class="nav-fine">FINE JEWELRY</a>
    <a class="nav-time">TIMEPIECES</a>
    <a class="nav-acc">ACCESSORIES</a>
    <a class="nav-des">DESIGNERS</a>
    <a class="nav-sale">SALE</a>
  </nav>

  <section class="hero" aria-label="Graduation gift sale banner">
    <div class="hero-products" role="img" aria-label="Photo of a diamond and sapphire heart pendant on a chain, a pearl ring and a two-tone gold band on a soft peach watercolor sky"></div>
    <div class="hero-copy">
      <div class="hero-script">Graduation</div>
      <div class="hero-gift">GIFT ON</div>
      <div class="hero-sale">SALE!</div>
    </div>
    <div class="hero-cap" role="img" aria-label="Glittering gold graduation cap illustration"></div>
  </section>

</body>
</html>
```